Business Card Design

We are a radiology group

We are working to move into new service centers

We want to communicate innovation and bringing our customers ahead with technology and outstanding results
Updates

I have uploaded a high resolution logo as requested :-)

Target Market(s)

hospitals, clinics

Industry/Entity Type

Business

Contact Information for Business Card

Deborah L. Pettigrew, MBA, CIIP
CTIO
deborah.pettigrew@tdrpc-mail.com
cell 518-476-2913
www.tdrpc-mail.com
Tidewater Diagnostic Radiology, PC

```html
<!DOCTYPE html>
<html lang="en">
<head>
<meta charset="utf-8">
<title>Tidewater Diagnostic Radiology – Business Card</title>
<link href="https://fonts.googleapis.com/css2?family=Barlow:wght@400;500;600&display=swap" rel="stylesheet">
<style>
  :root {
    --backdrop: #ededed;
    --card: #ffffff;
    --brand-blue: #1a8fd6;
    --scan-blue: #b9d2e6;
    --scan-blue-deep: #8fb1cf;
    --photo-dark: #1c2434;
    --photo-mid: #3d5f8c;
    --text-grey: #555a60;
    --icon-grey: #5d6166;
    --white: #ffffff;
  }
  * { margin: 0; padding: 0; box-sizing: border-box; }
  html, body { width: 1200px; height: 977px; overflow: hidden; background: var(--backdrop); }
  body { font-family: "Barlow", Arial, sans-serif; position: relative; }

  .business-card {
    position: absolute; left: 150px; top: 231px;
    width: 900px; height: 514px;
    background: var(--card);
    box-shadow: 0 6px 18px rgba(0,0,0,0.12);
    overflow: hidden;
  }
  .card-art { position: absolute; inset: 0; }

  .company-name {
    position: absolute; left: 470px; top: 80px;
    font-size: 21px; font-weight: 500; letter-spacing: 0.5px;
    font-variant: small-caps; color: var(--text-grey);
  }
  .holder-name {
    position: absolute; left: 398px; top: 160px;
    font-size: 28px; font-weight: 600; color: var(--white);
  }
  .holder-credentials {
    position: absolute; left: 398px; top: 198px;
    font-size: 22px; font-weight: 400; color: var(--white);
  }
  .contact-list { position: absolute; left: 420px; top: 270px; list-style: none; }
  .contact-item {
    display: flex; align-items: center; gap: 10px;
    height: 36px; font-size: 20px; color: var(--text-grey);
  }
  .contact-icon { width: 22px; height: 22px; flex: none; }
</style>
</head>
<body>
  <article class="business-card">
    <svg class="card-art" width="900" height="514" viewBox="0 0 900 514">
      <defs>
        <linearGradient id="scanTone" x1="0" y1="0" x2="1" y2="1">
          <stop offset="0" stop-color="var(--scan-blue-deep)"/>
          <stop offset="0.5" stop-color="var(--scan-blue)"/>
          <stop offset="1" stop-color="var(--scan-blue-deep)"/>
        </linearGradient>
        <linearGradient id="photoTone" x1="0" y1="0" x2="1" y2="0">
          <stop offset="0" stop-color="var(--photo-mid)"/>
          <stop offset="0.6" stop-color="var(--photo-dark)"/>
          <stop offset="1" stop-color="var(--photo-mid)"/>
        </linearGradient>
      </defs>
      <polygon class="scan-panel" role="img" aria-label="Light blue collage of brain scan images"
               points="0,0 315,0 450,514 0,514" fill="url(#scanTone)"/>
      <polygon class="brand-band" points="352,140 900,140 900,240 378,240" fill="var(--brand-blue)"/>
      <polygon class="consult-photo" role="img" aria-label="Photo of a doctor reviewing scan results with a patient"
               points="130,204 369,204 420,400 130,400" fill="url(#photoTone)"/>
    </svg>

    <div class="company-name">Tidewater Diagnostic Radiology</div>
    <h1 class="holder-name">Deborah L. Pettigrew</h1>
    <p class="holder-credentials">MBA | CIIP CTIO</p>

    <ul class="contact-list">
      <li class="contact-item">
        <svg class="contact-icon" viewBox="0 0 22 22"><circle cx="11" cy="11" r="11" fill="var(--icon-grey)"/><rect x="7.5" y="5" width="7" height="12" rx="1.5" fill="none" stroke="#fff" stroke-width="1.5"/></svg>
        518-476-2913
      </li>
      <li class="contact-item">
        <svg class="contact-icon" viewBox="0 0 22 22"><circle cx="11" cy="11" r="11" fill="var(--icon-grey)"/><rect x="5.5" y="7" width="11" height="8" fill="none" stroke="#fff" stroke-width="1.4"/><polyline points="5.5,7 11,12 16.5,7" fill="none" stroke="#fff" stroke-width="1.4"/></svg>
        deborah.pettigrew@tdrpc-mail.com
      </li>
      <li class="contact-item">
        <svg class="contact-icon" viewBox="0 0 22 22"><circle cx="11" cy="11" r="11" fill="var(--icon-grey)"/><circle cx="11" cy="11" r="6" fill="none" stroke="#fff" stroke-width="1.3"/><line x1="5" y1="11" x2="17" y2="11" stroke="#fff" stroke-width="1.2"/><ellipse cx="11" cy="11" rx="2.6" ry="6" fill="none" stroke="#fff" stroke-width="1.2"/></svg>
        www.tdrpc-mail.com
      </li>
    </ul>
  </article>
</body>
</html>
```